Business Cards for a small business advisory (business services)

Professional look. Same as would apply for a lawyer, accountant, or other financial services professional. Please use the logo colors

Target Market(s)

small business owners

Industry/Entity Type

Financial Servics

Contact Information for Business Card

Name: Gavin L. Whitmore, CAIA / Title: Business Advisor / Office #: (718) 294-7716 / Mobile #: (917) 382-5047 / Email: g.whitmore@clearfieldventurepartners.example / Web: www.clearfieldventurepartners.example

Font styles to use
Sans Serif

```html
<!DOCTYPE html>
<html lang="en">
<head>
<meta charset="utf-8">
<title>Clearfield Venture Partners – Business Cards</title>
<link rel="stylesheet" href="https://fonts.googleapis.com/css2?family=Montserrat:wght@400;500;600;700;800&display=swap">
<style>
  :root {
    --navy: #1b3a6b;
    --green: #7cb83f;
    --paper: #ffffff;
    --backdrop: #b3b3b3;
    --ink: #1b3a6b;
  }
  * { box-sizing: border-box; margin: 0; padding: 0; }
  html, body { width: 1200px; height: 900px; overflow: hidden; }
  body {
    background: var(--backdrop);
    font-family: "Montserrat", sans-serif;
    color: var(--ink);
    display: flex;
    flex-direction: column;
    align-items: center;
    justify-content: center;
    gap: 40px;
  }
  .card {
    width: 720px;
    height: 411px;
    background: var(--paper);
    border-bottom: 5px solid var(--navy);
    box-shadow: 0 6px 18px rgba(0,0,0,0.25);
    position: relative;
  }
  /* contact side */
  .card--contact {
    display: flex;
    align-items: center;
    padding: 0 48px;
  }
  .brand {
    display: flex;
    align-items: center;
    gap: 12px;
  }
  .brand__mark {
    width: 34px; height: 34px; border-radius: 50%;
    background: var(--navy);
    flex: none;
  }
  .brand__name {
    font-weight: 700;
    color: var(--navy);
    line-height: 1.05;
  }
  .brand__descriptor {
    font-weight: 600;
    color: var(--green);
    letter-spacing: 0.12em;
    text-transform: uppercase;
  }
  .brand__tagline {
    font-weight: 700;
    color: var(--navy);
    letter-spacing: 0.05em;
    text-transform: uppercase;
    white-space: nowrap;
  }
  .card--contact .brand-block { width: 290px; flex: none; }
  .card--contact .brand__name { font-size: 25px; }
  .card--contact .brand__descriptor { font-size: 10px; margin-top: 6px; }
  .card--contact .brand__tagline { font-size: 5.5px; letter-spacing: 0.02em; margin-top: 4px; }

  .divider {
    width: 1.5px;
    height: 230px;
    background: var(--navy);
    margin: 0 22px 0 14px;
    flex: none;
  }
  .details { font-size: 13px; line-height: 1.45; }
  .details__name { font-size: 21px; font-weight: 700; color: var(--navy); }
  .details__title { font-size: 13px; font-weight: 500; margin-bottom: 16px; }
  .details__address { margin-bottom: 16px; font-weight: 500; }
  .details__list { list-style: none; font-weight: 500; }
  .details__list li { display: flex; align-items: center; gap: 9px; white-space: nowrap; }
  .details__list svg { width: 13px; height: 13px; fill: var(--navy); flex: none; }

  /* logo side */
  .card--logo {
    display: flex;
    align-items: center;
    justify-content: center;
  }
  .card--logo .brand { gap: 22px; }
  .card--logo .brand__mark { width: 72px; height: 72px; }
  .card--logo .brand__name { font-size: 50px; }
  .card--logo .brand__descriptor { font-size: 18px; margin-top: 8px; }
  .card--logo .brand__tagline { font-size: 11px; margin-top: 6px; }
</style>
</head>
<body>

  <section class="card card--contact">
    <div class="brand-block">
      <div class="brand">
        <span class="brand__mark"></span>
        <div>
          <div class="brand__name">Clearfield</div>
          <div class="brand__descriptor">Venture Partners</div>
          <div class="brand__tagline">Practical guidance to buy, sell or grow your local business</div>
        </div>
      </div>
    </div>
    <div class="divider"></div>
    <div class="details">
      <div class="details__name">Gavin L. Whitmore, CAIA</div>
      <div class="details__title">Business Advisor</div>
      <div class="details__address">480 Ridgeview Parkway, Ste<br>210 Chattanooga, TN 37411</div>
      <ul class="details__list">
        <li><svg viewBox="0 0 24 24"><path d="M6.6 10.8a15 15 0 0 0 6.6 6.6l2.2-2.2a1 1 0 0 1 1-.25 11.4 11.4 0 0 0 3.6.57 1 1 0 0 1 1 1V20a1 1 0 0 1-1 1A17 17 0 0 1 3 4a1 1 0 0 1 1-1h3.5a1 1 0 0 1 1 1c0 1.25.2 2.450.57 3.57a1 1 0 0 1-.25 1z"/></svg>(718) 294-7716</li>
        <li><svg viewBox="0 0 24 24"><path d="M7 1h10a2 2 0 0 1 2 2v18a2 2 0 0 1-2 2H7a2 2 0 0 1-2-2V3a2 2 0 0 1 2-2zm0 3v14h10V4zm5 15.5a1 1 0 1 0 0 2 1 1 0 0 0 0-2z"/></svg>(917) 382-5047</li>
        <li><svg viewBox="0 0 24 24"><path d="M2 5h20v14H2zm2 2v.5l8 5 8-5V7zm0 2.8V17h16V9.8l-8 5z"/></svg>g.whitmore@clearfieldventurepartners.example</li>
        <li><svg viewBox="0 0 24 24"><path d="M12 2a10 10 0 1 0 0 20 10 10 0 0 0 0-20zm6.9 6h-3a15 15 0 0 0-1.3-3.6A8 8 0 0 1 18.9 8zM12 4c.8 1.2 1.5 2.5 1.9 4h-3.8c.4-1.5 1.1-2.8 1.9-4zM4.3 14a8 8 0 0 1 0-4h3.4a16 16 0 0 0 0 4zm.8 2h3a15 15 0 0 0 1.3 3.6A8 8 0 0 1 5.1 16zm3-8h-3a8 8 0 0 1 4.3-3.6A15 15 0 0 0 8.1 8zM12 20c-.8-1.2-1.5-2.5-1.9-4h3.8c-.4 1.5-1.1 2.8-1.9 4zm2.3-6H9.7a14 14 0 0 1 0-4h4.6a14 14 0 0 1 0 4zm.3 5.6a15 15 0 0 0 1.3-3.6h3a8 8 0 0 1-4.3 3.6zM16.3 14a16 16 0 0 0 0-4h3.4a8 8 0 0 1 0 4z"/></svg>www.clearfieldventurepartners.example</li>
      </ul>
    </div>
  </section>

  <section class="card card--logo">
    <div class="brand">
      <span class="brand__mark"></span>
      <div>
        <div class="brand__name">Clearfield</div>
        <div class="brand__descriptor">Venture Partners</div>
        <div class="brand__tagline">Practical guidance to buy, sell or grow your local business</div>
      </div>
    </div>
  </section>

</body>
</html>
```